Refer a friend or family in July 2014

We offer the following classrooms to suit ALL your needs.

Please put in table or in a clear format so parents can read this information

Before school care $35 or after rebates $17.50 per morning
Long day / vacation care $110 per day or after rebates $55.00 per day
Early morning Half day / vacation care (6.00am to 2.30pm) $80 per day or after rebates $40 per day
Half day / vacation care $60 per day (8.30am to 2.00pm) or after rebates $30 per day Vacation care half day 6am to 12pm or 12pm to 5.30pm $55 or $27.50 after rebates
After school care $45.00 or after rebate $22.50 per day

* Terms and Conditions – Family Referral Form
1. Offer valid till 31 August 2014
2. New Child must be enrolled for a minimum of 2 days per week and a 4 week period minimum before credit is applied
3. The $50 account credit will be added 5 weeks after referring family/families have started at Gathering Sprouts Velvet Otters Junior Education Centre.
4. The credit cannot be refunded as cash and is only a credit on their current account.
5. Discount offer applies only to all new referred children.
6. Existing children enrolled or siblings of current families at the centre are not eligible for this offer.

Target Market(s)

parents

Industry/Entity Type

School

Font styles to use
Sans Serif

Requirements
Must have
• refer a friend or family in July !

childcare local to you.

children learn, laugh and have fun!

be professional and corporate over "colourful and too childcare like " this is for parents

flexible times to suit you.

qualified teachers

get ready for school program - pre -kindergarten classroom

www.gatheringsprouts-example.com.au

0461735208
Should not have
• too much colour to messy - unclear..

```html
<!DOCTYPE html>
<html lang="en">
<head>
<meta charset="utf-8">
<title>Gathering Sprouts Velvet Otters – Refer a Friend Flyer</title>
<link rel="stylesheet" href="https://fonts.googleapis.com/css2?family=Lobster&family=Open+Sans:wght@400;600;700;800&display=swap">
<style>
  :root {
    --stage: #3a3a3c;
    --cream: #efe9dc;
    --cream-deep: #e2d9c6;
    --purple: #7a2f8c;
    --purple-light: #a24bb5;
    --purple-deep: #4a0f57;
    --plum-band: #5a0f4f;
    --yellow: #f7d417;
    --gold: #f4b73a;
    --green: #7fae3a;
    --green-dark: #5f8a26;
    --green-stitch: #b9d98a;
    --white: #ffffff;
    --ink: #3b2a20;
    --grey: #6d6d6d;
  }
  * { box-sizing: border-box; margin: 0; padding: 0; }
  html, body { width: 1200px; height: 750px; overflow: hidden; }
  body { background: var(--stage); position: relative; font-family: 'Open Sans', sans-serif; }

  .flyer {
    position: absolute; left: 430px; top: 15px;
    width: 340px; height: 720px; overflow: hidden;
    background: var(--cream);
  }

  .web-tab {
    position: absolute; top: 10px; right: 0; width: 232px; height: 20px;
    background: var(--purple); color: var(--white);
    border-radius: 10px 0 0 10px;
    font-size: 9.5px; font-weight: 600; line-height: 20px; padding-left: 14px;
  }

  .brand { position: absolute; top: 36px; left: 16px; right: 10px; display: flex; gap: 8px; align-items: flex-start; }
  .brand-dot { width: 28px; height: 28px; border-radius: 50%; background: var(--purple-light); flex: none; margin-top: 2px; }
  .brand-name { font-weight: 700; font-size: 12px; line-height: 1.2; color: var(--purple); }
  .brand-tagline { font-size: 9px; color: var(--grey); margin-top: 2px; }

  .kids-photo {
    position: absolute; top: 82px; left: 0; width: 340px; height: 150px;
    background: radial-gradient(ellipse at 50% 55%, #d9a88a 0%, #b78a6e 35%, #9a8f6a 55%, var(--cream-deep) 85%);
  }

  .offer {
    position: absolute; top: 228px; left: 0; width: 340px; height: 362px;
    background: radial-gradient(ellipse at 50% 25%, var(--purple-light) 0%, var(--purple) 50%, var(--purple-deep) 100%);
  }

  .ribbon { position: absolute; top: 204px; left: 6px; width: 328px; height: 50px; }
  .ribbon-text {
    position: absolute; top: 208px; left: 0; width: 340px; text-align: center;
    font-family: 'Lobster', cursive; font-size: 25px; color: var(--yellow); line-height: 40px;
  }

  .headline { position: absolute; top: 258px; left: 0; width: 340px; text-align: center; color: var(--white); }
  .headline-month { font-size: 16px; font-weight: 700; }
  .headline-intro { font-size: 11px; font-weight: 600; margin-top: 2px; }
  .headline-needs { font-size: 16px; font-weight: 800; line-height: 1.15; }

  .rates { position: absolute; top: 318px; left: 16px; width: 308px; border-collapse: collapse; }
  .rates td { border-bottom: 1px solid rgba(255,255,255,0.8); padding: 3px 0; vertical-align: middle; }
  .rate-name { color: var(--yellow); font-size: 9.5px; font-weight: 700; line-height: 1.2; width: 148px; }
  .rate-hours { display: block; color: var(--white); font-size: 8px; font-weight: 400; }
  .rate-price { color: var(--yellow); font-size: 11px; font-weight: 700; text-align: right; white-space: nowrap; }
  .rate-rebate { color: var(--white); font-size: 8.5px; font-weight: 400; }
  .rates-note { position: absolute; top: 502px; left: 16px; color: var(--white); font-size: 7.5px; }

  .features {
    position: absolute; top: 518px; left: 16px; width: 308px;
    list-style: none; display: grid; grid-template-columns: 1fr 1fr; gap: 4px 10px;
    color: var(--white); font-size: 9px; font-weight: 600; line-height: 1.2;
  }
  .features li { display: flex; gap: 5px; align-items: flex-start; }
  .features svg { flex: none; width: 10px; height: 10px; margin-top: 1px; }
  .features .wide { grid-column: 1 / 3; }

  .call-band {
    position: absolute; top: 590px; left: 0; width: 340px; height: 36px;
    background: var(--plum-band); color: var(--white);
    font-size: 15px; font-weight: 700; line-height: 36px; text-align: center;
  }
  .call-number { color: var(--yellow); font-size: 16px; }

  .terms {
    position: absolute; top: 626px; left: 0; width: 340px; height: 94px;
    background: var(--gold); color: var(--ink);
    font-size: 7.2px; line-height: 1.3; padding: 6px 14px;
  }
  .terms-title { font-weight: 700; }
  .terms ol { list-style: none; }
  .terms li { display: inline; }
</style>
</head>
<body>
  <main class="flyer">
    <div class="web-tab">www.gatheringsprouts-example.com.au</div>

    <header class="brand">
      <span class="brand-dot"></span>
      <div>
        <p class="brand-name">Gathering Sprouts Velvet Otters Junior Education Centre</p>
        <p class="brand-tagline">Where children laugh, learn and have fun!</p>
      </div>
    </header>

    <div class="kids-photo" role="img" aria-label="Photo of four smiling, laughing young children standing together"></div>

    <section class="offer"></section>

    <svg class="ribbon" viewBox="0 0 328 50" aria-hidden="true">
      <polygon points="0,12 22,6 22,44 0,46 10,28" fill="var(--green-dark)"/>
      <polygon points="328,12 306,6 306,44 328,46 318,28" fill="var(--green-dark)"/>
      <rect x="18" y="2" width="292" height="42" rx="2" fill="var(--green)"/>
      <line x1="24" y1="7" x2="304" y2="7" stroke="var(--green-stitch)" stroke-width="1.2" stroke-dasharray="4 3"/>
      <line x1="24" y1="39" x2="304" y2="39" stroke="var(--green-stitch)" stroke-width="1.2" stroke-dasharray="4 3"/>
    </svg>
    <p class="ribbon-text">Refer a friend or family*</p>

    <div class="headline">
      <p class="headline-month">in July 2014</p>
      <p class="headline-intro">We offer the following classrooms to suit</p>
      <p class="headline-needs">ALL your needs.</p>
    </div>

    <table class="rates">
      <tr><td class="rate-name">Before School Care</td><td class="rate-price">$35 per morning <span class="rate-rebate">(or $17.50*)</span></td></tr>
      <tr><td class="rate-name">Long Day / Vacation Care</td><td class="rate-price">$110 per day <span class="rate-rebate">(or $55*)</span></td></tr>
      <tr><td class="rate-name">Early Morning Half Day / Vacation Care<span class="rate-hours">(6.00am to 2.30pm)</span></td><td class="rate-price">$80 per day <span class="rate-rebate">(or $40*)</span></td></tr>
      <tr><td class="rate-name">Half Day / Vacation Care<span class="rate-hours">(8.30am to 2.00pm)</span></td><td class="rate-price">$60 per day <span class="rate-rebate">(or $30*)</span></td></tr>
      <tr><td class="rate-name">Vacation Care Half Day<span class="rate-hours">(6am to 12pm or 12pm to 5.30pm)</span></td><td class="rate-price">$55 per day <span class="rate-rebate">(or $27.50*)</span></td></tr>
      <tr><td class="rate-name">After School Care</td><td class="rate-price">$45 per day <span class="rate-rebate">(or $22.50*)</span></td></tr>
    </table>
    <p class="rates-note">* Price after rebates.</p>

    <ul class="features">
      <li><svg viewBox="0 0 10 10" aria-hidden="true"><path d="M1 5l3 3 5-7" fill="none" stroke="var(--yellow)" stroke-width="1.8"/></svg>Childcare local to you</li>
      <li><svg viewBox="0 0 10 10" aria-hidden="true"><path d="M1 5l3 3 5-7" fill="none" stroke="var(--yellow)" stroke-width="1.8"/></svg>Flexible times to suit you</li>
      <li><svg viewBox="0 0 10 10" aria-hidden="true"><path d="M1 5l3 3 5-7" fill="none" stroke="var(--yellow)" stroke-width="1.8"/></svg>Qualified teachers</li>
      <li><svg viewBox="0 0 10 10" aria-hidden="true"><path d="M1 5l3 3 5-7" fill="none" stroke="var(--yellow)" stroke-width="1.8"/></svg>Get ready for school program</li>
      <li class="wide"><svg viewBox="0 0 10 10" aria-hidden="true"><path d="M1 5l3 3 5-7" fill="none" stroke="var(--yellow)" stroke-width="1.8"/></svg>Pre-kindergarten classroom</li>
    </ul>

    <div class="call-band">Call <span class="call-number">0461735208</span> to find out more!</div>

    <footer class="terms">
      <p><span class="terms-title">*Terms and Conditions – Family Referral:</span>
        1. Offer valid till 31 August 2014.
        2. New child must be enrolled for a minimum of 2 days per week and a 4 week period minimum before credit is applied.
        3. The $50 account credit will be added 5 weeks after referring family/families have started at Gathering Sprouts Velvet Otters Junior Education Centre.
        4. The credit cannot be refunded as cash and is only a credit on their current account.
        5. Discount offer applies only to all new referred children.
        6. Existing children enrolled or siblings of current families at the centre are not eligible for this offer.</p>
    </footer>
  </main>
</body>
</html>
```